Business Card Design Project for Web Development Company

Need a professional card that stands out with both color and texture.
We provide websites and web development services for small businesses with a focus on connections. Examples include: Automotive repair shop, we take their repair logs and make them available online so their customers can view, print and share (when selling) their maintenance records. Vet clinic, we create systems where customers can sign up for a recurring payment program for the annual wellness checks on their pets and get reminders when it's time, then see and schedule their own appointments. Etc... So not simply a website, but one that connects systems or customers to the business.
Important - !!!!We will be using http://inkvaleprinters.com/ for the cards, so take a look at what options are available for business card printing, they can do a lot of cool things!!!!
You can pick any 1-3 options from inkvaleprinters. I'm leaning towards a black background, but the logo will work on any color.
Front:
Marcus Telford
2750 SW 8th Ave STE 214-587
Alder Falls, OR 97804
541-617-2038 - cell
541-259-7306 - office
marcus@sitelinkhub.com
www.SiteLinkHub.com
Updates
We provide websites and web development services for small businesses with a focus on connections. Examples include: Automotive repair shop, we take their repair logs and make them available online so their customers can view, print and share (when selling) their maintenance records. Vet clinic, we create systems where customers can sign up for a recurring payment program for the annual wellness checks on their pets and get reminders when it''s time, then see and schedule their own appointments. Etc... So not simply a website, but one that connects systems or customers to the business.
Target Market(s)
Small business owners
Industry/Entity Type
Automotive
Look and feel
Each slider illustrates characteristics of the customer's brand and the style your logo design should communicate.

```html
<!DOCTYPE html>
<html lang="en">
<head>
<meta charset="utf-8">
<title>SiteLinkHub Business Card</title>
<link href="https://fonts.googleapis.com/css2?family=Arimo:wght@400;700&display=swap" rel="stylesheet">
<style>
  :root {
    --page-bg: #e4e2df;
    --card-bg: #4a4a4a;
    --art-grey: #565656;
    --art-dark: #3e3e3e;
    --art-blue: #1b95d6;
    --text-light: #f1f1f1;
    --text-muted: #e2e2e2;
    --brand-blue: #1b95d6;
  }
  * { margin: 0; padding: 0; box-sizing: border-box; }
  html, body {
    width: 1200px; height: 1000px; overflow: hidden;
    background: var(--page-bg);
    font-family: "Arimo", Arial, sans-serif;
  }
  .card {
    position: absolute; left: 110px; top: 220px;
    width: 980px; height: 560px;
    background: var(--card-bg);
    box-shadow: 0 10px 30px rgba(0,0,0,0.25);
    overflow: hidden;
  }
  .feature-art {
    position: absolute; left: 21px; top: 23px;
    width: 441px; height: 447px;
    background: linear-gradient(135deg, var(--art-grey) 0%, var(--art-dark) 45%, var(--art-blue) 75%, var(--art-grey) 100%);
    opacity: 0.9;
  }
  .brand-name {
    position: absolute; right: 39px; top: 62px;
    font-size: 74px; font-weight: 700; line-height: 1;
    color: var(--brand-blue); letter-spacing: 1px;
  }
  .contact { position: absolute; left: 516px; top: 218px; }
  .contact__name {
    font-size: 46px; font-weight: 700; color: var(--text-light);
    line-height: 1; margin-bottom: 20px;
  }
  .contact__first { color: var(--brand-blue); }
  .contact__line {
    font-size: 24px; color: var(--text-muted);
    line-height: 49.5px;
  }
  .footer-link {
    position: absolute; top: 518px;
    font-size: 24px; color: var(--text-muted); line-height: 1;
  }
  .footer-link--email { left: 30px; }
  .footer-link--web { right: 28px; }
</style>
</head>
<body>
  <div class="card">
    <div class="feature-art" role="img" aria-label="Decorative artwork in grey and blue"></div>

    <div class="brand-name">SiteLinkHub</div>

    <div class="contact">
      <div class="contact__name"><span class="contact__first">Marcus</span> Telford</div>
      <div class="contact__line">2750 SW 8th Ave STE 214-587</div>
      <div class="contact__line">Alder Falls, OR 97804</div>
      <div class="contact__line">541-617-2038 - cell</div>
      <div class="contact__line">541-259-7306 - office</div>
    </div>

    <div class="footer-link footer-link--email">marcus@sitelinkhub.com</div>
    <div class="footer-link footer-link--web">www.SiteLinkHub.com</div>
  </div>
</body>
</html>
```